Modes of Action Brochure/Handout

We need an innovative, professional design for a multi page presentation of our research findings. We want a clean, fresh layout, want to utilize a couple photos we have bought and included in the example we put together for a starting point.. We want it to read easily.

Target Market(s)

Dietary Supplement Industry

Industry/Entity Type

It Professional

Requirements
Must have
• Attention getting, attractive.

```html
<!DOCTYPE html>
<html lang="en">
<head>
<meta charset="utf-8">
<title>NovaLac 10 – Modes of Action Brochure</title>
<link href="https://fonts.googleapis.com/css2?family=Arimo:wght@400;700&family=Tinos:wght@400;700&display=swap" rel="stylesheet">
<style>
:root{
  --stage:#202020;
  --red:#b5001f;
  --red-deep:#8e0016;
  --white:#ffffff;
  --ink:#2a2a2a;
  --photo-warm:#c98a6a;
  --photo-cool:#9fb2c4;
  --dusk-a:#2c3966;
  --dusk-b:#e9b27a;
}
*{box-sizing:border-box;margin:0;padding:0}
html,body{width:1200px;height:1137px;overflow:hidden;background:var(--stage)}
.canvas{position:relative;width:1200px;height:1137px}

/* cover */
.cover{position:absolute;left:285px;top:110px;width:342px;height:550px;background:var(--white);overflow:hidden}
.cover-photo{position:absolute;left:0;top:60px;width:342px;height:430px;background:linear-gradient(160deg,var(--photo-cool),#e8e8ea 45%,var(--photo-warm))}
.cover-band{position:absolute;left:0;top:0;width:342px;height:200px}
.brand-box{position:absolute;left:12px;top:24px;width:120px;height:32px;background:var(--white);border-radius:8px;display:flex;align-items:center;justify-content:center}
.brand{font-family:"Arimo",Arial,sans-serif;font-weight:700;font-size:19px;color:var(--red)}
.tagline{position:absolute;left:10px;top:62px;font-family:"Arimo",Arial,sans-serif;font-size:8px;color:var(--white);white-space:nowrap}
.cover-foot{position:absolute;left:0;bottom:0;width:342px;height:95px;background:var(--red)}
.cover-foot p{position:absolute;left:22px;font-family:"Tinos",serif;font-size:6.5px;color:var(--white);line-height:9px;white-space:nowrap}

/* references */
.refs{position:absolute;left:675px;top:113px;width:367px;height:472px;overflow:hidden;background:var(--white)}
.refs-photo{position:absolute;inset:0 0 6px 0;background:linear-gradient(150deg,#f3f3f3 30%,#c9d4df 60%,var(--photo-warm))}
.refs-rule{position:absolute;left:0;bottom:0;width:100%;height:6px;background:var(--red)}
.refs-label{position:absolute;left:14px;top:38px;width:144px;height:16px;background:var(--red);color:var(--white);font-family:"Tinos",serif;font-weight:700;font-size:10px;padding:2px 6px}
.refs-panel{position:absolute;left:14px;top:58px;width:340px;height:380px;background:rgba(255,255,255,.78);border-radius:10px;padding:6px 8px}
.refs-panel ol{list-style:none;font-family:"Arimo",Arial,sans-serif;font-size:6px;line-height:15.5px;color:var(--ink)}
.refs-panel li{white-space:nowrap}

/* inner spread */
.spread{position:absolute;left:150px;top:680px;width:910px;height:420px;background:var(--red);overflow:hidden}
.spread-photo-a{position:absolute;left:315px;top:0;width:150px;height:420px;background:linear-gradient(180deg,var(--dusk-a),#6a5a7a 55%,#3a3240)}
.spread-photo-b{position:absolute;left:465px;top:0;width:145px;height:420px;background:linear-gradient(180deg,#f4d9b4,var(--dusk-b) 50%,#8b6a52)}
.spread-frame{position:absolute;left:0;top:0}
.panel{position:absolute;top:0;height:420px;padding:12px 14px;color:var(--white);font-family:"Tinos",serif}
.panel-left{left:0;width:312px}
.panel-right{left:612px;width:298px}
.head{display:inline-block;background:var(--white);color:var(--red);font-family:"Tinos",serif;font-size:10.5px;font-weight:700;padding:1px 8px;margin:6px 0 3px}
.body{font-size:7px;line-height:9px}
.body b{font-weight:700}
.icon{float:left;width:56px;height:40px;margin:2px 8px 2px 0;border:1px solid var(--white)}
.icon.cells{background:linear-gradient(135deg,#3d4a66,#b24040)}
.icon.key{background:linear-gradient(135deg,#7fb6c2,#c7a878)}
.lead{font-size:9px;font-weight:700;line-height:11px}
.clear{clear:both}
</style>
</head>
<body>
<div class="canvas">

  <section class="cover" aria-label="Brochure cover">
    <div class="cover-photo" role="img" aria-label="Photo of a smiling couple in winter coats and red scarves"></div>
    <svg class="cover-band" width="342" height="200" viewBox="0 0 342 200">
      <path d="M0 0H342V10L235 82Q120 140 0 190Z" fill="#b5001f"/>
    </svg>
    <div class="brand-box"><span class="brand">NovaLac 10</span></div>
    <p class="tagline">High Priority Support for Immunity and Good Health</p>
    <footer class="cover-foot">
      <p style="top:42px">Crestline Nutrient Labs, LLC</p>
      <p style="top:52px">1420 Harbor Vale Rd, Suite 300 Millbrook, CA 90000, 555 010-2040/555 010-2041 FAX</p>
      <p style="top:62px">www.novalac10.example</p>
    </footer>
  </section>

  <section class="refs" aria-label="References page">
    <div class="refs-photo" role="img" aria-label="Photo of a young couple embracing with soft heart shapes"></div>
    <div class="refs-rule"></div>
    <h2 class="refs-label">References:</h2>
    <div class="refs-panel">
      <ol>
        <li>1. Food and the Method of Extracting the Same from</li>
        <li>Colostrum and Milk (US Patent 0,000,111)</li>
        <li>2. Method of Producing Antibodies in Milk (US Patent 0,000,222)</li>
        <li>3. Immunodynamic Complexes and Methods for Using and</li>
        <li>Preparing Such Complexes (Patent Application Pending)</li>
        <li>4. Northfield Clinical Associates. The Use of NovaLac 10 in Conjunction with a Holistic Treatment</li>
        <li>Model for Natural Killer Cell Stimulation in Chronic Illness. July 1998.</li>
        <li>5. Meridian Research, Inc. A Study of the Effects of Oral Dietary Supplementation of NovaLac 10</li>
        <li>Upon Natural Killer Cell Activity in a Healthy Human Population. Journal of Population Health</li>
        <li>Control, Vol 13, No 6, Dec 2009. 717-719.</li>
        <li>6. Vantage Immune Consultants, Inc. Examination of Immune Response Modulation in Humans by</li>
        <li>NovaLac 10 Utilizing a Double Blind Study. Jan 2001</li>
        <li>7. Marlow JA. Examination of Immune Response Modifiers in Healthy Individuals as Compared to</li>
        <li>the Refined Lacteal Complex NovaLac 10. Wellspring Letter, 2006;12 90-96.</li>
        <li>8. Scientific References: Amino Acid Sequencing of NovaLac 10 at Halden University</li>
        <li>9. Marlow J, Ortiz D, Bellamy DW. A Pilot Study of an anti-MRSA Bio-Engineered Lacteal Complex</li>
        <li>(anti-MRSA BLC) in a Murine Septicemia Model. Annals of Host Defense</li>
        <li>Research, 28: 1-7, 2006.</li>
        <li>10. Varga M, Lindqvist E, Moreau A, Tanaka M, Hale L. Evaluation of bovine-derived lacteal</li>
        <li>complex (NovaLac 10) supplementation on Gene Expression in BALB/c Mice. Bulletin of Applied</li>
        <li>Nutrient Science, 2011:3 89-92.</li>
        <li>11. Holm G, Ramirez D, Whitlock K. A novel extract from bovine colostrum whey supports innate</li>
        <li>immune functions. II. Rapid changes in cellular immune function in humans. Preventive</li>
      </ol>
    </div>
  </section>

  <section class="spread" aria-label="Inner spread">
    <div class="spread-photo-a" role="img" aria-label="Photo of a couple on a beach at dusk with glowing lanterns"></div>
    <div class="spread-photo-b" role="img" aria-label="Photo of two silhouettes forming a heart with their arms at sunset"></div>
    <svg class="spread-frame" width="910" height="420" viewBox="0 0 910 420">
      <line x1="315" y1="0" x2="315" y2="420" stroke="#e6d200" stroke-width="1.5"/>
      <line x1="465" y1="0" x2="465" y2="420" stroke="#e6d200" stroke-width="1.5"/>
      <line x1="610" y1="0" x2="610" y2="420" stroke="#e6d200" stroke-width="1.5"/>
    </svg>

    <div class="panel panel-left">
      <h3 class="head">Modes of Action</h3>
      <div class="body"><div class="icon cells" role="img" aria-label="Illustration of immune cells"></div>Ground-breaking research, peer-reviewed patents, controlled human trials and published studies support its role in immune health and everyday wellness.</div>
      <div class="clear"></div>
      <h3 class="head">Important General Observation</h3>
      <p class="body">Its functions act on the immune system in a balanced way, supporting natural defenses without overstimulation, as seen across many published studies.</p>
      <h3 class="head">Executive Summary</h3>
      <div class="body"><div class="icon key" role="img" aria-label="Photo of a vintage key"></div>Traditional dietary supplements rarely match the targeted support this formula offers for immune and overall wellness.<br><br>NovaLac 10 is a unique, highly soluble, non-stimulatory molecular complex that supports the immune system and healthy communication between cells.</div>
      <div class="clear"></div>
      <h3 class="head">INNATE and ADAPTIVE IMMUNE SYSTEM</h3>
      <p class="lead">Supports normalized lymphocyte (B cell, T cell and NK cell) activity in vivo, ex vivo and in vitro.</p>
      <p class="body"><b>PHYSIOLOGY:</b> T cells are an essential component of the human adaptive immune system, guiding defense.</p>
      <p class="body"><b>PHYSIOLOGY:</b> T-cells are a type of white blood cell that circulate in our bodies, scanning for cellular abnormalities and infections every day.</p>
    </div>

    <div class="panel panel-right">
      <h3 class="head">INFLAMMATORY RESPONSE</h3>
      <p class="body">Provides direct support to a healthy inflammatory response.<br><b>PHYSIOLOGY:</b> Inflammation is the body's protective reaction to injury, helping remove harmful stimuli and begin healing.</p>
      <h3 class="head">APOPTOSIS</h3>
      <p class="body">Supports regulated apoptosis.<br><b>PHYSIOLOGY:</b> Regulated cell death clears damaged or unneeded cells, keeping tissues balanced and healthy over time.</p>
      <h3 class="head">CELLULAR COMMUNICATION</h3>
      <p class="body">Supports effective cellular communication.<br><b>PHYSIOLOGY:</b> Cell signaling lets cells sense their surroundings and respond correctly, supporting normal growth and immunity.</p>
      <h3 class="head">GENE EXPRESSION</h3>
      <p class="body">Supports significant up-regulation of genes associated with innate and adaptive immunity.<br><b>PHYSIOLOGY:</b> Gene expression turns stored genetic information into functional products that guide every cell's activity.</p>
      <h3 class="head">TH1/TH2 CELL REGULATION</h3>
      <p class="body"><b>PHYSIOLOGY:</b> Helper T cells direct other immune cells, keeping the balance between Th1 and Th2 responses steady.</p>
    </div>
  </section>

</div>
</body>
</html>
```